Bref créative
Stationery and Business Card for WH
Whitlow Holdings, LLC
Professional
Dwight K. Ostrander, PE
Principal
17 Maple Hollow Lane
Elkton, MD 21408
Dwight@WhitlowHoldingsLLC.example
www.social.example/WhitlowHoldingsLLC
Please see previous submission (Logo, Business Card, and Stationery for Whitlow Holdings, LLC). On that submission, we have a winner.
Please add tagline Professional Civil Engineering Services. Also, please update states to include Maryland, Pennsylvania and Delaware
This is my logo in AI

```html
<!DOCTYPE html>
<html lang="en">
<head>
<meta charset="utf-8">
<title>Whitlow Holdings, LLC — Stationery</title>
<link rel="stylesheet" href="https://fonts.googleapis.com/css2?family=Montserrat:wght@400;600&display=swap">
<style>
  :root {
    --navy: #1d4f91;
    --sky: #29a9e0;
    --paper: #ffffff;
    --backdrop: #f1f3f6;
    --ink: #4a5563;
    --edge: #e2e6ec;
  }
  * { margin: 0; padding: 0; box-sizing: border-box; }
  html, body { width: 1200px; height: 936px; overflow: hidden; }
  body {
    position: relative;
    background: var(--backdrop);
    font-family: "Montserrat", Arial, sans-serif;
    color: var(--ink);
  }
  .sheet {
    position: absolute;
    background: var(--paper);
    border: 1px solid var(--edge);
    overflow: hidden;
  }
  .sheet svg.swoosh { position: absolute; inset: 0; width: 100%; height: 100%; }
  .brand {
    position: absolute;
    display: flex;
    align-items: center;
    gap: 6px;
  }
  .brand-dot { border-radius: 50%; background: var(--sky); flex: none; }
  .brand-text { display: flex; flex-direction: column; }
  .brand-name {
    color: var(--navy);
    font-weight: 600;
    letter-spacing: 0.06em;
    text-transform: uppercase;
    white-space: nowrap;
  }
  .tagline {
    color: var(--sky);
    font-weight: 400;
    letter-spacing: 0.08em;
    white-space: nowrap;
  }
  .contact { position: absolute; font-size: 6px; line-height: 1.5; color: var(--ink); white-space: nowrap; }
  .states { color: var(--navy); font-weight: 600; }

  /* Letterhead */
  .letterhead { left: 183px; top: 56px; width: 390px; height: 558px; }
  .letterhead .brand { left: 22px; top: 36px; }
  .letterhead .brand-dot { width: 14px; height: 14px; }
  .letterhead .brand-name { font-size: 9px; }
  .letterhead .tagline { font-size: 5.5px; margin-top: 2px; }
  .letterhead .contact { left: 244px; top: 30px; }
  .watermark {
    position: absolute; left: 128px; top: 200px; width: 130px; height: 130px;
    background: radial-gradient(circle, #e6eef7 0%, #f4f7fb 60%, #ffffff 100%);
  }

  /* Folder */
  .folder { left: 634px; top: 38px; width: 482px; height: 576px; }
  .folder .brand { left: 0; right: 0; top: 210px; flex-direction: column; gap: 14px; }
  .folder .brand-dot { width: 70px; height: 70px; }
  .folder .brand-text { align-items: center; }
  .folder .brand-name { font-size: 38px; line-height: 1.1; text-align: center; }
  .folder .brand-name small { display: block; font-size: 17px; letter-spacing: 0.32em; }
  .folder .tagline { font-size: 11px; margin-top: 10px; }
  .folder .states-line { font-size: 9px; margin-top: 6px; letter-spacing: 0.12em; }

  /* Business cards */
  .card-front { left: 43px; top: 657px; width: 203px; height: 109px; }
  .card-front .brand { left: 10px; top: 9px; gap: 4px; }
  .card-front .brand-dot { width: 10px; height: 10px; }
  .card-front .brand-name { font-size: 6.5px; }
  .card-front .tagline { font-size: 3.8px; margin-top: 1px; }
  .card-front .holder { position: absolute; left: 10px; top: 42px; font-size: 5px; line-height: 1.5; }
  .card-front .holder strong { color: var(--navy); font-weight: 600; }
  .card-front .contact { left: 98px; top: 42px; font-size: 4.3px; }
  .card-back { left: 43px; top: 779px; width: 203px; height: 109px; border: none;
    background: linear-gradient(160deg, #2a64ab 0%, var(--navy) 70%); }

  /* Envelope */
  .envelope-front { left: 266px; top: 665px; width: 432px; height: 218px; }
  .envelope-front .brand { left: 18px; top: 16px; }
  .envelope-front .brand-dot { width: 14px; height: 14px; }
  .envelope-front .brand-name { font-size: 10px; }
  .envelope-front .tagline { font-size: 5.5px; margin-top: 2px; }
  .envelope-front .contact { left: 18px; top: 52px; }
  .envelope-back { left: 738px; top: 672px; width: 429px; height: 211px; }
  .envelope-back .web {
    position: absolute; right: 22px; top: 22px; font-size: 7px;
    color: #ffffff; letter-spacing: 0.12em;
  }
</style>
</head>
<body>

<section class="sheet letterhead">
  <div class="brand">
    <span class="brand-dot"></span>
    <span class="brand-text">
      <span class="brand-name">Whitlow Holdings, LLC</span>
      <span class="tagline">Professional Civil Engineering Services</span>
    </span>
  </div>
  <div class="contact">
    17 Maple Hollow Lane<br>
    Elkton, MD 21408<br>
    P: 410.555.0173<br>
    Dwight@WhitlowHoldingsLLC.example<br>
    www.social.example/WhitlowHoldingsLLC<br>
    <span class="states">Maryland · Pennsylvania · Delaware</span>
  </div>
  <div class="watermark" role="img" aria-label="Faint brand watermark area"></div>
  <svg class="swoosh" viewBox="0 0 390 558" preserveAspectRatio="none" aria-hidden="true">
    <path d="M390,430 C372,505 300,545 222,558 L390,558 Z" fill="var(--navy)"/>
    <path d="M390,468 C380,520 345,548 300,558 L390,558 Z" fill="var(--sky)"/>
  </svg>
</section>

<section class="sheet folder">
  <svg class="swoosh" viewBox="0 0 482 576" preserveAspectRatio="none" aria-hidden="true">
    <path d="M335,0 C395,14 455,55 482,120 L482,0 Z" fill="var(--navy)"/>
    <path d="M410,0 C445,22 470,55 482,92 L482,0 Z" fill="var(--sky)"/>
  </svg>
  <div class="brand">
    <span class="brand-dot"></span>
    <span class="brand-text">
      <span class="brand-name">Whitlow<small>Holdings, LLC</small></span>
      <span class="tagline">Professional Civil Engineering Services</span>
      <span class="tagline states-line">Maryland · Pennsylvania · Delaware</span>
    </span>
  </div>
</section>

<section class="sheet card-front">
  <div class="brand">
    <span class="brand-dot"></span>
    <span class="brand-text">
      <span class="brand-name">Whitlow Holdings, LLC</span>
      <span class="tagline">Professional Civil Engineering Services</span>
    </span>
  </div>
  <div class="holder"><strong>Dwight K. Ostrander, PE</strong><br>Principal</div>
  <div class="contact">
    17 Maple Hollow Lane<br>
    Elkton, MD 21408<br>
    Dwight@WhitlowHoldingsLLC.example<br>
    <span class="states">MD · PA · DE</span>
  </div>
  <svg class="swoosh" viewBox="0 0 203 109" preserveAspectRatio="none" aria-hidden="true">
    <path d="M203,78 C196,96 178,106 160,109 L203,109 Z" fill="var(--navy)"/>
    <path d="M203,92 C199,101 190,107 182,109 L203,109 Z" fill="var(--sky)"/>
  </svg>
</section>

<section class="sheet card-back" aria-label="Business card reverse"></section>

<section class="sheet envelope-front">
  <div class="brand">
    <span class="brand-dot"></span>
    <span class="brand-text">
      <span class="brand-name">Whitlow Holdings, LLC</span>
      <span class="tagline">Professional Civil Engineering Services</span>
    </span>
  </div>
  <div class="contact">17 Maple Hollow Lane, Elkton, MD 21408 · <span class="states">Maryland · Pennsylvania · Delaware</span></div>
  <svg class="swoosh" viewBox="0 0 432 218" preserveAspectRatio="none" aria-hidden="true">
    <path d="M432,128 C410,182 350,210 286,218 L432,218 Z" fill="var(--navy)"/>
    <path d="M432,160 C420,196 390,212 356,218 L432,218 Z" fill="var(--sky)"/>
  </svg>
</section>

<section class="sheet envelope-back">
  <svg class="swoosh" viewBox="0 0 429 211" preserveAspectRatio="none" aria-hidden="true">
    <path d="M0,0 L429,0 L429,64 L70,64 C40,64 14,70 0,84 Z" fill="var(--navy)"/>
    <path d="M0,84 C14,70 40,64 70,64 L110,64 C70,66 30,78 0,100 Z" fill="var(--sky)"/>
  </svg>
  <span class="web">www.social.example/WhitlowHoldingsLLC</span>
</section>

</body>
</html>
```